Course flyer - evolutive design

We want to have a nice design for our course programm.
In fact we are school language, and our course programm change approximatively each 2 weeks§.
For that we need a design that we can modify each 2 weeks (only dates change ) by ourselves.
We used to have a classical design but we want to upgrade it with a modern and attractive design.
We can have 3 versions one for each city.
We have 3 offices: Tunis, Sousse & Sfax
Attached you can find old designs

Target Market(s)

students from 16 years old till retired people 76 years old

Industry/Entity Type

Education

Font styles to use
Sans Serif

Requirements
Must have
• clear timing for courses (date, days, timing)
• prices
• Adresse (each flyer has its own adress)
• phone Number
• Cool image
Should not have
• Racism
• Violence
• Too much stuff

```html
<!DOCTYPE html>
<html lang="fr">
<head>
<meta charset="utf-8">
<title>Cours d'allemand – Tunis – Mai / Juin 2016</title>
<link rel="stylesheet" href="https://fonts.googleapis.com/css2?family=Archivo+Black&family=Oswald:wght@500;700&family=Arimo:wght@400;700&display=swap">
<style>
  :root{
    --pink:#d14a9b;
    --yellow:#f6e63a;
    --lime:#c9dc3a;
    --white:#ffffff;
    --flag-black:#1d1416;
    --flag-red:#d4202a;
    --flag-gold:#e8b21a;
  }
  *{margin:0;padding:0;box-sizing:border-box}
  html,body{width:846px;height:1200px;overflow:hidden;background:var(--pink)}
  .flyer{position:relative;width:846px;height:1200px;background:var(--pink);overflow:hidden;font-family:"Arimo",Arial,sans-serif;color:var(--white)}

  .hero-band{position:absolute;left:0;top:0;width:846px;height:315px;
    background:linear-gradient(165deg,var(--flag-black) 0%,#3a1a1c 22%,var(--flag-red) 40%,#b81a22 55%,var(--flag-red) 64%,#e0701c 76%,var(--flag-gold) 90%,#c98f12 100%)}

  .brand{position:absolute;left:42px;top:125px;display:flex;align-items:center;gap:10px}
  .brand-dot{width:26px;height:26px;border-radius:50%;background:var(--lime)}
  .brand-name{font-family:"Arimo",Arial,sans-serif;font-weight:700;font-size:46px;line-height:1;color:var(--white);letter-spacing:-1px}

  .period{position:absolute;left:534px;top:32px;display:flex;color:var(--white)}
  .period-month{font-family:"Arimo",Arial,sans-serif;font-weight:700;font-size:21px;padding-right:6px;padding-top:3px}
  .period-side{border-left:1.5px solid var(--white);padding-left:5px}
  .period-side .juin{font-family:"Arimo",Arial,sans-serif;font-size:21px;line-height:1.1}
  .period-side .year{font-family:"Arimo",Arial,sans-serif;font-size:48px;line-height:.95;letter-spacing:-1px}

  .title{position:absolute;left:346px;top:250px;font-family:"Archivo Black",Arial,sans-serif;font-size:68px;line-height:62px;color:var(--white);letter-spacing:-2px;text-transform:uppercase}

  .schedule-col{position:absolute;width:180px;text-align:center;line-height:24.3px}
  .col-left{left:18px;top:372px}
  .col-right{left:169px;top:372px}
  .mode{font-family:"Oswald",Arial,sans-serif;font-weight:700;font-size:21px;color:var(--yellow);letter-spacing:.5px}
  .days,.dates{font-family:"Oswald",Arial,sans-serif;font-weight:700;font-size:16px;color:var(--yellow)}
  .time{font-family:"Oswald",Arial,sans-serif;font-weight:500;font-size:16px;color:var(--yellow);text-decoration:underline;text-underline-offset:3px}
  .module{font-family:"Oswald",Arial,sans-serif;font-weight:500;font-size:16px;color:var(--white)}
  .module b{font-weight:700}
  .spacer{height:24px}

  .new-course{margin:8px auto 10px;width:142px;border:2px solid var(--yellow);border-radius:10px;padding-bottom:4px;line-height:22px}
  .new-course .tag{background:var(--yellow);color:#1c1c1c;font-family:"Oswald",Arial,sans-serif;font-weight:700;font-size:16px;border-radius:7px 7px 0 0;margin:-1px -1px 2px}
  .business{font-family:"Oswald",Arial,sans-serif;font-weight:700;font-size:17px;color:var(--yellow)}

  .photo-ring{position:absolute;left:377px;top:407px;width:445px;height:445px;border-radius:50%;background:var(--lime);padding:12px}
  .photo-circle{width:100%;height:100%;border-radius:50%;background:radial-gradient(circle at 50% 50%,#c89a80 0%,#8d6450 35%,#3d2a24 70%,#6e4a3c 100%)}

  .notes{position:absolute;left:379px;top:844px;width:440px;font-family:"Arimo",Arial,sans-serif;font-weight:700;font-size:13.3px;line-height:16px;list-style:none}
  .notes li{padding-left:10px;text-indent:-10px;margin-bottom:6px}
  .notes li::before{content:"•";color:var(--yellow);margin-right:4px}
  .price{position:absolute;left:382px;top:934px;font-family:"Arimo",Arial,sans-serif;font-weight:700;font-size:13.3px;color:var(--yellow)}

  .city{position:absolute;left:380px;top:966px;font-family:"Archivo Black",Arial,sans-serif;font-size:57px;line-height:1;letter-spacing:-1px}
  .address{position:absolute;left:383px;top:1036px;font-family:"Arimo",Arial,sans-serif;font-weight:700;font-size:11.6px;line-height:14.2px;font-style:normal}
  .address .note{font-weight:400;font-style:italic}
  .contact{position:absolute;left:383px;top:1100px;font-family:"Arimo",Arial,sans-serif;font-weight:700;font-size:11.6px;line-height:15px}
  .social{position:absolute;left:382px;top:1131px;display:flex;align-items:center;gap:10px;font-family:"Arimo",Arial,sans-serif;font-weight:700;font-size:11.6px}
  .social-square{width:22px;height:22px;background:#2f4f96;border-radius:3px}

  .figure{position:absolute;left:730px;top:878px;width:100px;height:318px;border-radius:40px 40px 6px 6px;background:linear-gradient(180deg,#e8c6a8 0%,#d8d0be 22%,#cfc7b3 50%,#3e5577 62%,#2c3e5c 100%)}
</style>
</head>
<body>
<div class="flyer">
  <div class="hero-band" role="img" aria-label="Drapeau allemand flottant en noir, rouge et or"></div>

  <div class="brand">
    <span class="brand-dot"></span>
    <span class="brand-name">lingora group</span>
  </div>

  <div class="period">
    <div class="period-month">MAI</div>
    <div class="period-side"><div class="juin">JUIN</div><div class="year">2016</div></div>
  </div>

  <h1 class="title">Cours<br>d'allemand</h1>

  <div class="schedule-col col-left">
    <div class="mode">INTENSIF</div>
    <div class="days">(Lundi - Vendredi)</div>
    <div class="dates">07/03 - 25/03</div>
    <div class="time">09H30 - 12H30</div>
    <div class="module"><b>A1.1</b> DK2090</div>
    <div class="module"><b>A1.2</b> DK2091</div>
    <div class="module"><b>A2.1</b> DK2092</div>
    <div class="module"><b>A2.2</b> DK2093</div>
    <div class="module"><b>B2.1</b> DK2094</div>
    <div class="time">13H00 - 16H00</div>
    <div class="module"><b>A1.1</b> DK2095</div>
    <div class="module"><b>A1.2</b> DK2096</div>
    <div class="module"><b>A2.1</b> DK2097</div>
    <div class="module"><b>B1.1</b> DK2098</div>
    <div class="module"><b>B1.2</b> DK2099</div>
    <div class="spacer"></div>
    <div class="mode">INTENSIF</div>
    <div class="days">(Lundi - Vendredi)</div>
    <div class="dates">28/03 - 15/04</div>
    <div class="time">09H30 - 12H30</div>
    <div class="module"><b>A1.1</b> DK2105</div>
    <div class="module"><b>A1.2</b> DK2106</div>
    <div class="module"><b>A2.1</b> DK2107</div>
    <div class="module"><b>A2.2</b> DK2108</div>
    <div class="module"><b>B2.1</b> DK2109</div>
    <div class="spacer" style="height:6px"></div>
    <div class="time">13H00 - 16H00</div>
    <div class="module"><b>A1.1</b> DK2110</div>
    <div class="module"><b>A1.2</b> DK2111</div>
    <div class="module"><b>B1.1</b> DK2112</div>
    <div class="module"><b>B1.2</b> DK2113</div>
    <div class="module"><b>C1.1</b> DK2114</div>
  </div>

  <div class="schedule-col col-right">
    <div class="mode">EXTENSIF</div>
    <div class="days">(Lun / Mer / Ven)</div>
    <div class="dates">29/02 - 25/03</div>
    <div class="time">18H30 - 21H30</div>
    <div class="module"><b>A1.1</b> DK2101</div>
    <div class="module"><b>A1.2</b> DK2102</div>
    <div class="module"><b>A2.1</b> DK2103</div>
    <div class="new-course">
      <div class="tag">NOUVEAU COURS:</div>
      <div class="business">BUSINESS-DEUTSCH</div>
      <div class="module"><b>A1.1</b> DK2101</div>
    </div>
    <div class="spacer" style="height:14px"></div>
    <div class="dates">28/03 - 22/04</div>
    <div class="module"><b>A1.1</b> DK2121</div>
    <div class="module"><b>A1.2</b> DK2122</div>
    <div class="module"><b>A2.1</b> DK2123</div>
    <div class="module"><b>A2.2</b> DK2124</div>
    <div class="business" style="margin-top:6px">BUSINESS-DEUTSCH</div>
    <div class="module"><b>A1.1</b> DK2125</div>
    <div class="module"><b>A1.2</b> DK2126</div>
    <div class="spacer" style="height:12px"></div>
    <div class="mode">EXTENSIF</div>
    <div class="days">(Mardi / Jeudi)</div>
    <div class="dates">28/03 - 05/05</div>
    <div class="time">18H30 - 21H30</div>
    <div class="module"><b>A1.1</b> DK2115</div>
    <div class="module"><b>A1.2</b> DK2116</div>
    <div class="module"><b>A2.1</b> DK2117</div>
    <div class="module"><b>A2.2</b> DK2118</div>
    <div class="module"><b>B1.1</b> DK2119</div>
    <div class="module"><b>B1.2</b> DK2120</div>
  </div>

  <div class="photo-ring">
    <div class="photo-circle" role="img" aria-label="Groupe de jeunes étudiants souriants, têtes réunies en cercle, vus d'en haut"></div>
  </div>

  <ul class="notes">
    <li>Toute inscription doit impérativement se faire au plus tard une semaine avant le début des cours.</li>
    <li>Nombre minimum de 4 participants requis.</li>
    <li>L'horaire des cours est susceptible d'être modifié.</li>
  </ul>
  <div class="price">Prix par module 340 TND.</div>

  <div class="city">TUNIS</div>
  <address class="address">
    Imm. Les Palmiers, 3<sup>ème</sup> étage<br>
    8 Rue du Lac Léman<br>
    <span class="note">(en face de l'Hôtel Marina)</span><br>
    1053 Les Berges du Lac 1
  </address>
  <div class="contact">
    Tel: +216 71 000 482<br>
    Email: tunis@lingora.org - Web: www.lingora.org
  </div>
  <div class="social">
    <span class="social-square"></span>
    <span>www.social.com/lingora</span>
  </div>

  <div class="figure" role="img" aria-label="Jeune homme souriant avec sacoche, faisant un signe de la main"></div>
</div>
</body>
</html>
```